Help our Crumb Parlour find our winning design! We're looking for a business card....

We’re a Crumb Parlour in NY specializing in custom-made cakes and unique desserts.
Our cakes combine flavor and art, each designed to match customer’s special event and theme.
We’d like a unique business card with a clean design that will combine French chic and artistic look & feel.
We’d like to differentiate ourselves from standard bakeries, please don’t offer cupcake images :-)
Our logo is peach-pink and brown and we’d love to use these colors ( . Another color that can be added is gold - or feel free to suggest!

Target Market(s)

Women, ages 25-55

Industry/Entity Type

Boutique

Contact Information for Business Card

Text on card:
Logo
Crumb Parlour by Dana Whitfield

www.xxxxxxxx.com
xxx@xxxxx.com
(516) xxx-xxxx
F – xxxxxxxxxx
IG - xxxxxxxxx

Font styles to use
Sans Serif
Script

Requirements
Must have
• Logo
• Clean look
• French chic and artistic look & feel.
Nice to have
• Damask pattern
Should not have
• Cupcake images

```html
<!DOCTYPE html>
<html lang="en">
<head>
<meta charset="utf-8">
<title>Velvet Tier – Business Card</title>
<link rel="stylesheet" href="https://fonts.googleapis.com/css2?family=Cormorant+Garamond:wght@500;600&family=Montserrat:wght@600&display=swap">
<style>
  :root {
    --peach: #eea797;
    --peach-light: #f5c2b6;
    --cocoa: #3b2620;
    --cream: #ffffff;
    --page: #ffffff;
  }
  * { margin: 0; padding: 0; box-sizing: border-box; }
  html, body {
    width: 1200px;
    height: 1075px;
    overflow: hidden;
    background: var(--page);
  }
  .canvas {
    position: relative;
    width: 1200px;
    height: 1075px;
  }
  .card {
    position: absolute;
    width: 630px;
    background: var(--peach);
    overflow: hidden;
    color: var(--cocoa);
    font-family: "Cormorant Garamond", Georgia, serif;
  }
  .card--front { left: 118px; top: 16px; height: 351px; }
  .card--back  { left: 121px; top: 455px; height: 348px; }

  /* Front */
  .flourish-frame {
    position: absolute;
    left: 14px; top: 46px;
    width: 600px; height: 256px;
    border-radius: 120px;
    background: var(--peach-light);
  }
  .brand-name {
    position: absolute;
    left: 0; right: 0; top: 180px;
    text-align: center;
    font-weight: 500;
    font-size: 60px;
    line-height: 1;
    letter-spacing: 1px;
  }
  .tagline {
    position: absolute;
    left: 0; right: 0; top: 284px;
    text-align: center;
    font-family: "Montserrat", Arial, sans-serif;
    font-weight: 600;
    font-size: 15px;
    letter-spacing: 3.5px;
  }

  /* Back */
  .corner-flourish {
    position: absolute;
    background: var(--peach-light);
  }
  .corner-flourish--top-left    { left: 0; top: 0; width: 137px; height: 212px; border-bottom-right-radius: 90px; }
  .corner-flourish--bottom-left { left: 0; top: 256px; width: 88px; height: 92px; border-top-right-radius: 60px; }
  .corner-flourish--right       { right: 0; top: 0; width: 136px; height: 348px; border-top-left-radius: 70px; border-bottom-left-radius: 70px; }

  .contact {
    position: absolute;
    left: 0; right: 0;
    text-align: center;
    line-height: 1;
  }
  .contact__name    { top: 106px; font-size: 48px; font-weight: 500; }
  .contact__title   { top: 152px; font-size: 26px; font-weight: 500; }
  .contact__details { top: 202px; font-size: 23px; font-weight: 500; }
  .contact__web     { top: 237px; font-size: 23px; font-weight: 500; }
  .contact__sep {
    display: inline-block;
    width: 6px; height: 6px;
    margin: 0 9px 4px;
    border-radius: 50%;
    background: var(--cream);
  }
  .social {
    position: absolute;
    top: 311px;
    display: flex;
    align-items: center;
    gap: 7px;
    font-size: 17px;
    font-weight: 600;
  }
  .social--first  { left: 110px; }
  .social--second { left: 325px; }
  .social__mark {
    width: 17px; height: 17px;
    background: var(--cocoa);
    border-radius: 2px;
  }
</style>
</head>
<body>
<main class="canvas">

  <section class="card card--front" aria-label="Business card front">
    <div class="flourish-frame" role="img" aria-label="White ribbon swirl ornament framing the brand name"></div>
    <h1 class="brand-name">Velvet Tier</h1>
    <p class="tagline">HANDCRAFTED WITH LOVE</p>
  </section>

  <section class="card card--back" aria-label="Business card back">
    <div class="corner-flourish corner-flourish--top-left" role="img" aria-label="White ribbon swirl ornament"></div>
    <div class="corner-flourish corner-flourish--bottom-left" role="img" aria-label="White ribbon swirl ornament"></div>
    <div class="corner-flourish corner-flourish--right" role="img" aria-label="White ribbon swirl ornament"></div>

    <h2 class="contact contact__name">Dana Whitfield</h2>
    <p class="contact contact__title">Crumb Parlour</p>
    <p class="contact contact__details">(516) 555-0182<span class="contact__sep"></span>dana@VelvetTierNY.com</p>
    <p class="contact contact__web">www.VelvetTierNY.com</p>

    <div class="social social--first"><span class="social__mark"></span>VelvetTierNYCakes</div>
    <div class="social social--second"><span class="social__mark"></span>VelvetTierNYCakes</div>
  </section>

</main>
</body>
</html>
```